The Verlo Plan with Dr Hal (book cover)

I am Dr Hal. I have written a book on weight loss. The Verlo Plan. The book uses fasting, plant-based proteins, and walking to help its followers lose a great deal of weight and improve their health, functionality, and longevity. We need a new book cover. Please take the profile picture of my face, just my face, and transform it into an animation or sketch. There will be a duality. The left side will be left alone but the right side of the face will be turned into a modified picture of a Greek orthodox monk reflecting the origination of this fasting practice. I need a beard on the monk side. The background should be black. All in darkness. Under or above should be the title and author. Text. This book will be used on paperleaf and Brindlemart. Go to www.theverloplan.example
Updates

Target Market(s)

Middle age men and woman

Industry/Entity Type

Weight loss and wellness

Requirements
Must have
• Duality of face. Young man on left and monk on right. Sketch vs animation with black background
Nice to have
• Black back drop, crisp fonts
Should not have
• No smiles

```html
<!DOCTYPE html>
<html lang="en">
<head>
<meta charset="utf-8">
<title>The Verlo Plan — Book Cover</title>
<link href="https://fonts.googleapis.com/css2?family=Cinzel:wght@400;500&display=swap" rel="stylesheet">
<style>
  :root {
    --stage: #121112;
    --cover: #000000;
    --ink: #ffffff;
    --art-light: #d9d9d9;
    --art-dark: #3a3a3a;
  }
  * { margin: 0; padding: 0; box-sizing: border-box; }
  html, body {
    width: 1200px;
    height: 614px;
    overflow: hidden;
    background: var(--stage);
  }
  .stage {
    position: relative;
    width: 1200px;
    height: 614px;
    background: var(--stage);
  }
  .cover {
    position: absolute;
    left: 400px;
    top: 27px;
    width: 400px;
    height: 560px;
    background: var(--cover);
    border: 3px solid var(--ink);
    color: var(--ink);
    font-family: "Cinzel", "Trajan Pro", serif;
  }
  .rule {
    position: absolute;
    height: 2px;
    background: var(--ink);
  }
  .title-kicker {
    position: absolute;
    top: 40px;
    left: 0;
    width: 100%;
    text-align: center;
    font-size: 21px;
    line-height: 26px;
    letter-spacing: 1px;
  }
  .title-main {
    position: absolute;
    top: 64px;
    left: 0;
    width: 100%;
    text-align: center;
    font-size: 41px;
    line-height: 50px;
    font-weight: 400;
    letter-spacing: 1px;
  }
  .subtitle {
    position: absolute;
    top: 112px;
    left: 0;
    width: 100%;
    text-align: center;
    font-size: 10.5px;
    line-height: 14px;
    letter-spacing: 0.2px;
  }
  .portrait {
    position: absolute;
    left: 0;
    top: 0;
    width: 400px;
    height: 560px;
  }
  .author {
    position: absolute;
    top: 489px;
    left: 0;
    width: 100%;
    text-align: center;
    font-size: 29px;
    line-height: 36px;
    letter-spacing: 0.5px;
  }
  .credentials {
    position: absolute;
    top: 524px;
    left: 0;
    width: 100%;
    text-align: center;
    font-size: 13px;
    line-height: 16px;
    letter-spacing: 1px;
  }
</style>
</head>
<body>
  <main class="stage">
    <section class="cover">
      <div class="rule" style="left:55px; top:52px; width:114px;"></div>
      <div class="rule" style="left:229px; top:52px; width:116px;"></div>
      <p class="title-kicker">THE</p>
      <h1 class="title-main">VERLO PLAN</h1>
      <p class="subtitle">BEFORE THERE WAS KORWELL, THERE WAS VERLO</p>

      <svg class="portrait" viewBox="0 0 400 560" xmlns="http://www.w3.org/2000/svg">
        <defs>
          <linearGradient id="portrait-tone" x1="0" y1="0" x2="1" y2="0">
            <stop offset="0" stop-color="var(--art-light)"/>
            <stop offset="0.52" stop-color="#bdbdbd"/>
            <stop offset="1" stop-color="var(--art-dark)"/>
          </linearGradient>
        </defs>
        <rect role="img" aria-label="Split-face illustration: young man on the left half, bearded Greek orthodox monk on the right half"
              x="132" y="158" width="171" height="242" rx="70" fill="url(#portrait-tone)"/>
        <rect class="portrait-frame" x="200" y="145" width="147" height="325" fill="none" stroke="var(--ink)" stroke-width="2"/>
      </svg>

      <p class="author">DR HAL MARENKO</p>
      <div class="rule" style="left:74px; top:531px; width:75px;"></div>
      <div class="rule" style="left:253px; top:531px; width:79px;"></div>
      <p class="credentials">MD , MBA</p>
    </section>
  </main>
</body>
</html>
```